依頼詳細
メインビジュアルのイメージはお祭りで酢だこをかついでいるようなイメージです。イラストor写真可。ただ、上半身裸は芳しくなく、ハッピ等を着ている方が望ましいです。
一番下商品名・価格・注文数・「注文コード」の枠を設けてください。

納期が早く(納品6/17の週)、一度修正あり(6/14頃)。そのため、スムーズな作業・連絡を取れる方ご提案お待ちしております。

ご不明点あればお気軽にご質問お待ちしております。
記載項目
添付チラシ参照ください。
サイズ
A4
ページ数
片面
希望イメージ
シンプル 複雑
単色 カラフル
暗い 明るい
日常 高級
遊び心 厳粛
未来的 伝統的
女性的 男性的
希望する色
赤系、青系、緑系、黄・オレンジ系
納品ファイル
• イラストレーター形式 (.ai)
補足説明
必ずお入れするものではありませんが、酢だこの写真追加しておきます。必要であればお使いください。

イラストイメージがクライアントに合致しました。この度はありがとうございました。

質の高い多くのご提案いただきまして、ありがとうございました。
今後も案件ありますので、ぜひご参加お待ちしております。

```html
<!DOCTYPE html>
<html lang="ja">
<head>
<meta charset="utf-8">
<title>酢だこ 祭チラシ</title>
<link rel="stylesheet" href="https://fonts.googleapis.com/css2?family=Noto+Sans+JP:wght@400;700;900&family=Noto+Serif+JP:wght@700;900&display=swap">
<style>
:root{
  --red:#d7261e;
  --sky:#cfe9f7;
  --green:#2f8a3c;
  --light-green:#e6f2e3;
  --ink:#222;
  --title:#1d1d1d;
  --line:#6a9a6e;
  --white:#fff;
}
*{box-sizing:border-box;margin:0;padding:0}
html,body{width:853px;height:1200px;overflow:hidden;background:var(--white)}
body{font-family:"Noto Sans JP",sans-serif;color:var(--ink)}
.flyer{position:relative;width:853px;height:1200px;overflow:hidden;background:var(--white)}
.hero{position:absolute;left:0;top:0;width:853px;height:650px;background:linear-gradient(180deg,#eaf6fc 0%,var(--sky) 60%,#9fd0ee 100%)}
.lantern-string{position:absolute;left:0;top:0;width:853px;height:58px;background:linear-gradient(180deg,#f3c6c0,#f8e6d9)}
.origin-banner{position:absolute;left:300px;top:22px;width:500px;height:48px;background:var(--white);border:3px solid var(--red);border-radius:6px;display:flex;align-items:center;justify-content:center;font-weight:900;font-size:27px;color:var(--red);letter-spacing:1px}
.campaign{position:absolute;left:14px;top:78px;width:92px;height:92px;border-radius:50%;background:var(--white);border:3px solid var(--red);display:flex;flex-direction:column;align-items:center;justify-content:center;color:var(--red);font-weight:700;line-height:1.1;z-index:2}
.campaign small{font-size:10px;color:var(--green)}
.campaign strong{font-size:22px;font-weight:900}
.campaign span{font-size:10px}
.festival-art{position:absolute;left:40px;top:90px;width:500px;height:560px;border-radius:40% 40% 6% 6%;background:radial-gradient(circle at 50% 35%,#e8473a 0%,#c9261f 45%,#f2c29c 75%,rgba(242,194,156,0) 100%)}
.title{position:absolute;left:585px;top:95px;writing-mode:vertical-rl;font-family:"Noto Serif JP",serif;font-weight:900;font-size:132px;line-height:1;letter-spacing:2px;color:var(--title)}
.tagline{position:absolute;left:765px;top:150px;height:470px;writing-mode:vertical-rl;font-family:"Noto Serif JP",serif;font-weight:700;font-size:20px;line-height:1.5;letter-spacing:3px;color:var(--ink)}
.product-photo{position:absolute;left:585px;top:505px;width:180px;height:135px;border-radius:50% 50% 12px 12px/30% 30% 12px 12px;background:linear-gradient(180deg,#f1e3e0,#d9a79f)}
.offers{position:absolute;left:0;top:650px;width:853px;height:112px;background:var(--light-green);border-top:4px solid var(--green)}
.offer{position:absolute;top:12px;width:205px;height:88px;background:var(--white);border:2px solid var(--green)}
.offer--small{left:18px}.offer--large{left:232px}
.offer__head{display:flex;align-items:center;gap:6px;padding:6px 8px 0;font-weight:700;font-size:15px}
.offer__num{display:inline-flex;width:24px;height:24px;background:var(--green);color:var(--white);align-items:center;justify-content:center;font-weight:900}
.offer__price{padding:4px 10px 0;color:var(--red);font-weight:900;font-size:32px;line-height:1}
.offer__price small{font-size:11px;color:var(--ink);font-weight:400}
.customer{position:absolute;left:455px;top:10px;width:380px;border:1px solid var(--line);background:var(--white)}
.customer__row{height:30px;border-bottom:1px solid var(--line);font-size:11px;padding:8px 8px;color:#555}
.customer__row:last-child{border-bottom:none}
.order{position:absolute;left:18px;top:782px;width:817px}
.order__code{display:flex;height:34px;border:2px solid var(--green)}
.order__code-label{width:120px;background:var(--green);color:var(--white);font-weight:700;display:flex;align-items:center;justify-content:center;font-size:15px}
.order__code-value{flex:1;display:flex;align-items:center;padding-left:12px;font-weight:700;font-size:15px}
.order__info{margin:12px 0 14px;font-size:15px;line-height:1.6}
.order__info b{color:var(--red)}
.order-table{width:100%;border-collapse:collapse;font-size:20px}
.order-table th{background:var(--green);color:var(--white);font-weight:700;height:40px;border:1px solid var(--green)}
.order-table td{height:78px;border:1px solid var(--line);padding:0 14px}
.order-table td.no{width:50px;text-align:center;font-weight:900;background:var(--light-green)}
.order-table td.price{width:220px;text-align:right}
.order-table td.qty{width:160px}
.footnote{position:absolute;left:18px;top:1120px;width:817px;font-size:11px;color:#555;display:flex;justify-content:space-between}
</style>
</head>
<body>
<main class="flyer">
  <section class="hero">
    <div class="lantern-string" role="img" aria-label="祭りの提灯が連なる飾り"></div>
    <div class="origin-banner">本場 000 からお届けします!</div>
    <div class="festival-art" role="img" aria-label="ハッピ姿の子どもたちが大きな酢だこを担ぐ祭りのイラスト"></div>
    <div class="campaign"><small>キャンペーン期間</small><strong>0/0(0)</strong><span>まで</span></div>
    <h1 class="title">酢だこ</h1>
    <p class="tagline">風味豊かに仕上げた美味しい酢だこをぜひお試し下さい。</p>
    <div class="product-photo" role="img" aria-label="容器入り酢だこの商品写真"></div>
  </section>

  <section class="offers">
    <div class="offer offer--small">
      <div class="offer__head"><span class="offer__num">1</span>酢だこ(無頭)400g</div>
      <div class="offer__price">3,380円<small>(税込)</small></div>
    </div>
    <div class="offer offer--large">
      <div class="offer__head"><span class="offer__num">2</span>酢だこ(無頭)800g</div>
      <div class="offer__price">5,780円<small>(税込)</small></div>
    </div>
    <div class="customer">
      <div class="customer__row">お名前</div>
      <div class="customer__row">ご住所</div>
      <div class="customer__row">お電話番号</div>
    </div>
  </section>

  <section class="order">
    <div class="order__code">
      <div class="order__code-label">注文コード</div>
      <div class="order__code-value">2019.08 酢だこ祭</div>
    </div>
    <p class="order__info">ご注文受付期間:<b>7/19(金)~20(土)まで</b><br>お届け予定日:<b>8/7(水)から順次配送</b></p>
    <table class="order-table">
      <thead><tr><th></th><th>商品名 / 規格</th><th>価格</th><th>注文数</th></tr></thead>
      <tbody>
        <tr><td class="no">1.</td><td>酢だこ(無頭) / 400g</td><td class="price">3,380円(税込)</td><td class="qty"></td></tr>
        <tr><td class="no">2.</td><td>酢だこ(無頭) / 800g</td><td class="price">5,780円(税込)</td><td class="qty"></td></tr>
      </tbody>
    </table>
  </section>

  <p class="footnote"><span>※商品の写真はイメージです。数量に限りがございます。</span><span>価格は消費税込みです。</span></p>
</main>
</body>
</html>
```